Stationery Design

Need a stationery design for an established accounting firm based in London, England.

The company’s name is ‘Harold Brinkley’. We provide a broad range of bookkeeping, accounting, audit, tax and business services to a wide range of clients (ie, individuals, company, partnerships, etc).

The stationary design needs to show strength and trust and should be clean, corporate and professional.

Only 2 colours must be used as noted on the logo.

The fonts are in Optima

We need the following:

#1: Business Cards (design on 2 sides)
#2: Letterhead (word format) and can be sent to printers
#3: Continuation sheets (word format) and can be sent to printers
#4: Sales invoice template (word format) and can be sent to printers
#5: Report Cover front and back for binding,
#6: Complimentary Slips,
#7: Legal corners with our logo only
#7: Email signature templates

I have attached my company's logo in various file formats

We also need to have our accountancy association’s logo and this must be in the same colour as the dark blue. This PQTB logo must be at least 8mm square (can be larger). I have attached the PQTB logo in various file formats

I have also attached other information that you will need for the letter head and invoice templates

I have also attached our old letterhead, fee note template for reference
Updates

Dear Designers - I have increased the budget

Dear Designers - I have read your comments on the fact that the prize does not reflect the work. Thank you and I appreciate your comments. Unfortunately, I am a start up and my budget is limited. As an Alternative, I have reduced the work that I am asking for to the following items and I hope you can assist: #1: Business Cards (design on 2 sides) #2: Letterhead (word format) and can be sent to printers #3: Report Cover front and back for binding, #4: Email signature templates Regards

Industry/Entity Type

Accounting

```html
<!DOCTYPE html>
<html lang="en">
<head>
<meta charset="utf-8">
<title>Harold Brinkley Stationery</title>
<link href="https://fonts.googleapis.com/css2?family=Tenor+Sans&family=Lato:wght@400;700&display=swap" rel="stylesheet">
<style>
:root{
  --navy:#22386a;
  --purple:#7d1f6f;
  --ink:#3b3b45;
  --muted:#8a8a92;
  --rule:#c9c9cf;
  --paper:#ffffff;
  --band-a:#e8e6e2;
  --band-b:#f3f3f3;
}
*{box-sizing:border-box;margin:0;padding:0}
html,body{width:1200px;height:2506px;overflow:hidden}
body{position:relative;font-family:"Lato",sans-serif;color:var(--ink);background:var(--band-a)}
.band{position:absolute;left:0;width:1200px}
.band--sheets{top:0;height:835px;background:var(--band-a)}
.band--cards{top:835px;height:865px;background:var(--band-b)}
.band--envelope{top:1700px;height:806px;background:var(--band-a)}

.brand{display:flex;align-items:center;justify-content:center;gap:10px}
.brand-mark{background:var(--purple);flex:none}
.brand-name{font-family:"Tenor Sans",sans-serif;color:var(--navy);letter-spacing:.04em;white-space:nowrap;text-transform:uppercase}

.sheet{position:absolute;top:33px;width:552px;height:780px;background:var(--paper);box-shadow:0 2px 6px rgba(0,0,0,.18)}
.sheet--letter{left:33px}
.sheet--invoice{left:612px}
.sheet .brand{position:absolute;top:44px;left:0;right:0}
.sheet .brand-mark{width:18px;height:18px}
.sheet .brand-name{font-size:22px}

.member-badge{position:absolute;left:248px;top:640px;width:56px;height:56px;background:var(--navy)}
.sheet-footer{position:absolute;left:40px;right:40px;bottom:38px;text-align:center;font-size:6.5px;line-height:1.5;color:var(--ink)}
.sheet-footer strong{color:var(--navy)}

.invoice-meta{position:absolute;top:92px;right:50px;text-align:left;font-size:7px;line-height:1.5;color:var(--ink)}
.invoice-number{font-family:"Tenor Sans",sans-serif;font-size:13px;color:var(--navy);margin-bottom:3px}
.invoice-table{position:absolute;top:172px;left:40px;width:472px;border-collapse:collapse;font-size:6.5px}
.invoice-table th{font-weight:700;color:var(--navy);text-align:left;padding:0 4px 10px;font-size:7px}
.invoice-table td{vertical-align:top;padding:6px 4px 20px}
.invoice-table .col-no{width:34px;color:var(--navy);font-weight:700}
.invoice-table .col-desc{width:220px}
.invoice-table .col-price,.invoice-table .col-qty,.invoice-table .col-total{text-align:center}
.invoice-table .col-qty{border-right:1px solid var(--rule)}
.item-title{font-weight:700;color:var(--navy);font-size:7px;margin-bottom:2px}
.item-text{color:var(--muted);line-height:1.4}

.card{position:absolute;width:520px;height:320px;background:var(--paper);box-shadow:0 2px 8px rgba(0,0,0,.15)}
.card--front{left:50px;top:1105px}
.card--back{left:630px;top:1105px}
.card--front .brand{position:absolute;top:0;bottom:0;left:0;right:0}
.card--front .brand-mark{width:26px;height:26px}
.card--front .brand-name{font-size:32px}
.card--back .brand{position:absolute;top:30px;left:30px;justify-content:flex-start}
.card--back .brand-mark{width:16px;height:16px}
.card--back .brand-name{font-size:19px}
.card-person{position:absolute;top:110px;left:0;right:0;text-align:center}
.card-name{font-family:"Tenor Sans",sans-serif;font-size:36px;color:var(--navy);letter-spacing:.03em}
.card-role{font-family:"Tenor Sans",sans-serif;font-size:20px;color:var(--purple);margin-top:2px}
.card-address{position:absolute;left:30px;bottom:28px;font-size:11px;line-height:1.5;color:var(--ink)}
.card-contact{position:absolute;right:30px;bottom:28px;font-size:11px;line-height:1.5;color:var(--ink);text-align:right}

.envelope{position:absolute;left:150px;top:1880px;width:900px;height:420px;background:var(--paper);box-shadow:0 2px 8px rgba(0,0,0,.15)}
.envelope-flap{position:absolute;inset:0}
.envelope .brand{position:absolute;top:32px;left:0;right:0}
.envelope .brand-mark{width:22px;height:22px}
.envelope .brand-name{font-size:28px}
.envelope-address{position:absolute;top:90px;left:0;right:0;text-align:center;font-size:11px;line-height:1.5;color:var(--ink)}
</style>
</head>
<body>
<section class="band band--sheets">
  <article class="sheet sheet--letter">
    <div class="brand"><span class="brand-mark"></span><span class="brand-name">Harold Brinkley</span></div>
    <div class="member-badge" role="img" aria-label="Professional association membership badge"></div>
    <footer class="sheet-footer">
      <strong>Linden Court, 14 Marlow Yard, Kingsfield Road, Putney, London, SW15 2QT</strong><br>
      Tel: 020 7946 0183 &nbsp;·&nbsp; www.harold-brinkley.co.uk<br>
      Company registered in England and Wales, number 08451273.<br>
      Registered to carry on audit work in the United Kingdom by the association.
    </footer>
  </article>

  <article class="sheet sheet--invoice">
    <div class="brand"><span class="brand-mark"></span><span class="brand-name">Harold Brinkley</span></div>
    <div class="invoice-meta">
      <div class="invoice-number">Invoice No. 11097</div>
      Date: 06/05/2024<br>
      Account: HB-2044-0173<br>
      Reference: PB-0518-22
    </div>
    <table class="invoice-table">
      <thead>
        <tr><th class="col-no">#</th><th class="col-desc">Description</th><th class="col-price">Unit Price</th><th class="col-qty">Quantity</th><th class="col-total">Total</th></tr>
      </thead>
      <tbody>
        <tr><td class="col-no">01</td><td class="col-desc"><div class="item-title">Work Name Here</div><div class="item-text">Short summary of the service provided during the period, with any notes for the client about scope.</div></td><td class="col-price">$100</td><td class="col-qty">2</td><td class="col-total">$200</td></tr>
        <tr><td class="col-no">02</td><td class="col-desc"><div class="item-title">Work Name Here</div><div class="item-text">Short summary of the service provided during the period, with any notes for the client about scope.</div></td><td class="col-price">$100</td><td class="col-qty">2</td><td class="col-total">$200</td></tr>
        <tr><td class="col-no">03</td><td class="col-desc"><div class="item-title">Work Name Here</div><div class="item-text">Short summary of the service provided during the period, with any notes for the client about scope.</div></td><td class="col-price">$100</td><td class="col-qty">2</td><td class="col-total">$200</td></tr>
        <tr><td class="col-no">04</td><td class="col-desc"><div class="item-title">Work Name Here</div><div class="item-text">Short summary of the service provided during the period, with any notes for the client about scope.</div></td><td class="col-price">$100</td><td class="col-qty">2</td><td class="col-total">$200</td></tr>
        <tr><td class="col-no">05</td><td class="col-desc"><div class="item-title">Work Name Here</div><div class="item-text">Short summary of the service provided during the period, with any notes for the client about scope.</div></td><td class="col-price">$100</td><td class="col-qty">2</td><td class="col-total">$200</td></tr>
        <tr><td class="col-no">06</td><td class="col-desc"><div class="item-title">Work Name Here</div><div class="item-text">Short summary of the service provided during the period, with any notes for the client about scope.</div></td><td class="col-price">$100</td><td class="col-qty">2</td><td class="col-total">$200</td></tr>
      </tbody>
    </table>
    <footer class="sheet-footer">
      <strong>Linden Court, 14 Marlow Yard, Kingsfield Road, Putney, London, SW15 2QT</strong><br>
      Tel: 020 7946 0183 &nbsp;·&nbsp; www.harold-brinkley.co.uk<br>
      Bank: Sort code 40-12-76 &nbsp;·&nbsp; Account 31926819
    </footer>
  </article>
</section>

<section class="band band--cards"></section>
<article class="card card--front">
  <div class="brand"><span class="brand-mark"></span><span class="brand-name">Harold Brinkley</span></div>
</article>
<article class="card card--back">
  <div class="brand"><span class="brand-mark"></span><span class="brand-name">Harold Brinkley</span></div>
  <div class="card-person">
    <div class="card-name">MARTIN HALE</div>
    <div class="card-role">Manager</div>
  </div>
  <div class="card-address">Linden Court<br>14 Marlow Yard<br>Kingsfield Road<br>Putney, London<br>SW15 2QT</div>
  <div class="card-contact">Tel: 020 7946 0183<br>martin@harold-brinkley.co.uk</div>
</article>

<section class="band band--envelope"></section>
<article class="envelope">
  <svg class="envelope-flap" width="900" height="420" viewBox="0 0 900 420">
    <rect x="1" y="1" width="898" height="418" fill="none" stroke="#d2d2d6" stroke-width="2"/>
    <polyline points="2,2 450,250 898,2" fill="none" stroke="#d2d2d6" stroke-width="2"/>
    <polyline points="2,418 330,200" fill="none" stroke="#e0e0e3" stroke-width="2"/>
    <polyline points="898,418 570,200" fill="none" stroke="#e0e0e3" stroke-width="2"/>
  </svg>
  <div class="brand"><span class="brand-mark"></span><span class="brand-name">Harold Brinkley</span></div>
  <div class="envelope-address">
    Linden Court, 14 Marlow Yard, Kingsfield Road,<br>
    Putney, London, SW15 2QT<br>
    Tel: 020 7946 0183<br>
    www.harold-brinkley.co.uk
  </div>
</article>
</body>
</html>
```